Sleek modern site for stage hypnotist who does high school, college, university and corporate gigs.

Need a website design for stage hypnotist Mark Dolloway
I'm using a plinkio domain

Mark Dolloway is a stage hypnotist who does high school shows , colleges, corporate and fundraisers
Looking for something sleek and modern looking.
I need about 4 pages at least one main describing what i do
1st page Describes what events i do (high school, college, corporate, weddings, fundraisers, fairs)
2nd page would be an about/bio page
3rd FAQ page about hypnosis.

*what venues do you work with?
*how long is your show?
*How do we promote the show?
*is it safe
*are you insured?
*how much does it cost?
4th page will be a contact page and link to my social media like Snapvue, chirpnet, and possibly Friendlyn.

Included is a few pictures that I'll probably including on the site. I'm waiting on the rest for photoshoot at the this week. Some of these pictures probably will have different stock backgrounds other than grey (something like a las vegas strip or a stage.

Visually I'm looking for a cool color scheme.

Target Market(s)

High school for now but college and corporate down the road.

Industry/Entity Type

Entertainment Industry

Coding

Coded - Design and coding required

Number of Pages Required

4 page

Font styles to use
Serif
Sans Serif

Colors
3277b5
85acd3
9d9d9d
5c5c5c
cbcbcb
aaaaaa
1b1b1b
333333

Requirements
Must have
• MUST BE ABLE TO WORK WITH PLINKIO
• A sleek and professional look as if I've been doing this for years.
• The ability to edit the text of the site so i can improve upon the persuasive parts if need be.
• I also will be getting more promotional photos in the 5 or 6 days after the deadline days so if i pick your project i'd like to be able to integrate some of them into the design. The 3 photos i provided are somewhat place holders to give you an idea of the rest that are to come.
Nice to have
• drop down links
Should not have
• if you zoobit other stage hypnotists their sites are a bit stale and not that modern.

```html
<!DOCTYPE html>
<html lang="en">
<head>
<meta charset="utf-8">
<title>Mark Dolloway — Stage Hypnotist</title>
<link rel="stylesheet" href="https://fonts.googleapis.com/css2?family=Sorts+Mill+Goudy&family=Open+Sans:wght@400;600&display=swap">
<style>
  :root {
    --blue: #3277b5;
    --blue-light: #85acd3;
    --grey: #9d9d9d;
    --grey-dark: #5c5c5c;
    --grey-pale: #cbcbcb;
    --grey-mid: #aaaaaa;
    --ink: #1b1b1b;
    --charcoal: #333333;
    --white: #f2f2f2;
    --serif: "Sorts Mill Goudy", Georgia, serif;
    --sans: "Open Sans", Arial, sans-serif;
  }
  * { box-sizing: border-box; margin: 0; padding: 0; }
  html, body { width: 1200px; height: 3000px; overflow: hidden; background: var(--ink); }
  body { position: relative; font-family: var(--serif); color: var(--grey-pale); }

  .page { position: absolute; left: 0; width: 1200px; height: 750px; overflow: hidden; background: var(--ink); }
  .page--events { top: 0; }
  .page--about { top: 750px; }
  .page--faq { top: 1500px; }
  .page--contact { top: 2250px; }

  .site-nav { position: absolute; top: 0; left: 0; width: 100%; height: 40px; background: #1e1e1e; border-bottom: 1px solid #2b2b2b; z-index: 3; }
  .site-nav a { position: absolute; top: 10px; font-family: var(--serif); font-size: 19px; color: var(--grey); text-decoration: none; }
  .site-nav a.is-active { color: var(--blue); }
  .site-nav .nav-events { left: 96px; }
  .site-nav .nav-about { left: 216px; }
  .site-nav .nav-faq { left: 336px; }
  .site-nav .nav-contact { left: 452px; }

  .hero-backdrop { position: absolute; top: 40px; left: 0; width: 100%; height: 710px;
    background: linear-gradient(180deg, #262626 0%, #2e2e2e 40%, #3a3a3a 52%, #262626 66%, #1e1e1e 100%); }
  .portrait { position: absolute; z-index: 1;
    background: radial-gradient(ellipse at 50% 30%, #4a4a4a 0%, #2c2c2c 55%, #1d1d1d 100%); }
  .page--events .portrait { left: 600px; top: 40px; width: 520px; height: 710px; }
  .page--about .portrait { left: 620px; top: 40px; width: 460px; height: 710px; }

  .hero-name { position: absolute; left: 80px; top: 372px; font-size: 54px; font-weight: 400; color: var(--white); letter-spacing: 1px; z-index: 2; }
  .hero-role { position: absolute; left: 80px; width: 440px; top: 438px; text-align: right; font-size: 22px; color: var(--blue); letter-spacing: 1px; z-index: 2; }
  .events-title { position: absolute; left: 80px; top: 576px; font-size: 20px; color: var(--blue); letter-spacing: 2px; z-index: 2; }
  .events-list { position: absolute; left: 380px; width: 160px; top: 578px; list-style: none; text-align: center; z-index: 2; }
  .events-list li { font-size: 15px; line-height: 22px; color: var(--grey-pale); letter-spacing: 1px; }

  .section-title { position: absolute; left: 96px; font-size: 60px; font-weight: 400; color: var(--white); letter-spacing: 1px; z-index: 2; }
  .page--about .section-title { top: 1180px; top: 430px; }
  .about-copy { position: absolute; left: 212px; top: 524px; width: 400px; font-size: 19px; line-height: 26px; color: var(--blue); z-index: 2; }

  .band { position: absolute; top: 40px; left: 0; width: 100%; height: 110px; background: linear-gradient(180deg, #2c2c2c, #232323); }
  .page--faq .section-title { top: 180px; }
  .faq-list { position: absolute; left: 96px; top: 282px; width: 700px; list-style: none; }
  .faq-item { position: absolute; left: 0; display: flex; align-items: center; gap: 24px; font-size: 17px; color: var(--blue); white-space: nowrap; }
  .faq-item svg { width: 14px; height: 12px; fill: var(--blue); }
  .faq-item.is-open { color: var(--white); }
  .faq-item.is-open svg { fill: var(--white); }
  .faq-answer { position: absolute; left: 0; top: 100px; font-family: var(--sans); font-size: 11px; color: var(--grey-pale); white-space: nowrap; }

  .page--contact .section-title { top: 184px; left: 0; width: 688px; text-align: center; }
  .contact-form { position: absolute; left: 96px; top: 282px; width: 496px; }
  .field { position: absolute; left: 0; width: 496px; border: 1.5px solid var(--grey-pale); border-radius: 6px; background: #1d1d1d; }
  .field span { position: absolute; left: 14px; top: 7px; font-family: var(--sans); font-size: 10px; color: var(--blue); letter-spacing: 1px; }
  .field--name { top: 0; height: 48px; }
  .field--email { top: 68px; height: 48px; }
  .field--phone { top: 136px; height: 48px; }
  .field--message { top: 208px; height: 140px; }
  .submit { position: absolute; left: 336px; top: 380px; width: 160px; height: 36px; border: 0; border-radius: 6px; background: var(--blue-light); color: var(--white); font-family: var(--sans); font-size: 11px; font-weight: 600; letter-spacing: 1px; }
  .social { position: absolute; left: 862px; top: 320px; list-style: none; }
  .social li { position: absolute; left: 0; display: flex; align-items: center; gap: 12px; font-size: 22px; color: var(--blue); white-space: nowrap; }
  .social li::before { content: ""; width: 14px; height: 14px; border-radius: 50%; background: var(--blue); }
</style>
</head>
<body>

<section class="page page--events">
  <nav class="site-nav"><a class="nav-events is-active">Events</a><a class="nav-about">About</a><a class="nav-faq">FAQ</a><a class="nav-contact">Contact</a></nav>
  <div class="hero-backdrop"></div>
  <div class="portrait" role="img" aria-label="Photo of Mark Dolloway standing in a dark shirt against a grey studio backdrop"></div>
  <h1 class="hero-name">MARK DOLLOWAY</h1>
  <p class="hero-role">STAGE HYPNOTIST</p>
  <h2 class="events-title">EVENTS I DO</h2>
  <ul class="events-list">
    <li>HIGH SCHOOL</li><li>COLLEGE</li><li>CORPORATE</li><li>WEDDING</li><li>FUNDRAISERS</li><li>FAIRS</li>
  </ul>
</section>

<section class="page page--about">
  <nav class="site-nav"><a class="nav-events">Events</a><a class="nav-about is-active">About</a><a class="nav-faq">FAQ</a><a class="nav-contact">Contact</a></nav>
  <div class="hero-backdrop"></div>
  <div class="portrait" role="img" aria-label="Photo of Mark Dolloway reaching a hand toward the viewer against a grey backdrop"></div>
  <h2 class="section-title">ABOUT</h2>
  <p class="about-copy">Lorem ipsum dolor sit amet, consectetur adipiscing elit, sed do eiusmod tempor incididunt ut labore et dolore magna aliqua. Ut enim ad minim veniam, quis nostrud exercitation ullamco laboris nisi ut aliquip ex ea commodo consequat.</p>
</section>

<section class="page page--faq">
  <nav class="site-nav"><a class="nav-events">Events</a><a class="nav-about">About</a><a class="nav-faq is-active">FAQ</a><a class="nav-contact">Contact</a></nav>
  <div class="band"></div>
  <h2 class="section-title">FAQ</h2>
  <ul class="faq-list">
    <li class="faq-item" style="top:0">What venues do you work with?<svg viewBox="0 0 14 12"><path d="M0 0h14L7 12z"/></svg></li>
    <li class="faq-item is-open" style="top:76px">How long is your show?<svg viewBox="0 0 14 12"><path d="M0 12h14L7 0z"/></svg></li>
    <li class="faq-answer">Duis aute irure dolor in reprehenderit in voluptate velit esse cillum dolore eu fugiat nulla pariatur.</li>
    <li class="faq-item" style="top:142px">How do we promote the show?<svg viewBox="0 0 14 12"><path d="M0 0h14L7 12z"/></svg></li>
    <li class="faq-item" style="top:208px">Is it safe?<svg viewBox="0 0 14 12"><path d="M0 0h14L7 12z"/></svg></li>
    <li class="faq-item" style="top:284px">Are you insured?<svg viewBox="0 0 14 12"><path d="M0 0h14L7 12z"/></svg></li>
    <li class="faq-item" style="top:352px">How much does it cost?<svg viewBox="0 0 14 12"><path d="M0 0h14L7 12z"/></svg></li>
  </ul>
</section>

<section class="page page--contact">
  <nav class="site-nav"><a class="nav-events">Events</a><a class="nav-about">About</a><a class="nav-faq">FAQ</a><a class="nav-contact is-active">Contact</a></nav>
  <div class="band"></div>
  <h2 class="section-title">CONTACT</h2>
  <form class="contact-form">
    <div class="field field--name"><span>NAME:</span></div>
    <div class="field field--email"><span>E-MAIL:</span></div>
    <div class="field field--phone"><span>PHONE:</span></div>
    <div class="field field--message"><span>MESSAGE:</span></div>
    <button class="submit" type="button">SUBMIT</button>
  </form>
  <ul class="social">
    <li style="top:0">Friendlyn</li>
    <li style="top:132px">Snapvue</li>
    <li style="top:268px">chirpnet</li>
  </ul>
</section>

</body>
</html>
```